Grand Opening / Live Music Event

My band is playing a Grand Opening event on Saturday April 5th. I need a flyer utilizing the attached image of our bass player and incorporating our band logo. This picture makes me laugh and gives the impression he is angry - like saying "it's going to be a celebration fool!" or something along those lines. I need to the flyer to pop and present an image that it will be an excellent party. Feel free to incorporate any background or theme style. You can find other images of my band in the event they are needed at: https://www.velorumhub.example/Corkvalleyband

Some details:

The event will be at Quimby's Hall. 8241 Larkspur Ave. #204, Frisco, Texas. (214) 705-9183 for table reservations.

Saturday April 5th. Party starts at 7:00 PM with an acoustic set by the Velvet Otters and Cork Valley taking the stage at 10:00 PM.

Hottest new bar in Frisco! Drink specials all night with the Zephyr Pale girls, and great live music to celebrate this grand opening.

I will use this for FB and other online marketing, as well as some print.

```html
<!DOCTYPE html>
<html lang="en">
<head>
<meta charset="utf-8">
<title>Quimby's Hall Grand Opening – Cork Valley Live</title>
<link rel="stylesheet" href="https://fonts.googleapis.com/css2?family=Bungee+Inline&family=Righteous&family=Open+Sans:wght@700&display=swap">
<style>
  :root {
    --backdrop: #f1f2f3;
    --frame-blue: #1ba8ea;
    --deep-blue: #0d3f9e;
    --mid-blue: #2b7fd6;
    --sky-blue: #5cc3f2;
    --stage-dark: #14162e;
    --stage-red: #b0223a;
    --ink-white: #ffffff;
  }
  html, body {
    margin: 0;
    width: 872px;
    height: 1200px;
    overflow: hidden;
    background: var(--backdrop);
  }
  .flyer {
    position: absolute;
    left: 16px;
    top: 57px;
    width: 840px;
    height: 1086px;
    display: block;
  }
  .flyer__frame { fill: var(--frame-blue); }
  .flyer__rule { stroke: var(--ink-white); stroke-width: 1.6; }
  .headline {
    fill: var(--ink-white);
    font-family: "Righteous", sans-serif;
  }
  .headline--small { font-size: 21px; letter-spacing: 2px; }
  .headline--large { font-size: 25px; letter-spacing: 1.5px; }
  .venue-name {
    fill: var(--ink-white);
    font-family: "Bungee Inline", sans-serif;
    font-size: 40px;
  }
  .event-line {
    fill: var(--ink-white);
    font-family: "Righteous", sans-serif;
  }
  .event-line--lead { font-size: 24px; }
  .event-line--detail { font-size: 15px; letter-spacing: 1px; }
  .event-line--promo { font-size: 17px; letter-spacing: 1px; }
  .event-line--closing { font-size: 14px; letter-spacing: 1px; }
  .date {
    fill: var(--ink-white);
    font-family: "Bungee Inline", sans-serif;
  }
  .date--day { font-size: 62px; }
  .date--number { font-size: 120px; }
  .date--month { font-size: 48px; }
  .band-name {
    fill: var(--ink-white);
    font-family: "Righteous", sans-serif;
    font-size: 22px;
    letter-spacing: 1px;
  }
  .footer-line {
    fill: var(--ink-white);
    font-family: "Open Sans", sans-serif;
    font-weight: 700;
    font-size: 11.5px;
  }
  .panel--light { fill: var(--sky-blue); opacity: 0.45; }
  .panel--strip { fill: var(--ink-white); opacity: 0.12; }
</style>
</head>
<body>
<svg class="flyer" viewBox="0 0 674 871" xmlns="http://www.w3.org/2000/svg">
  <defs>
    <linearGradient id="stage-light" x1="0" y1="0" x2="1" y2="1">
      <stop offset="0" stop-color="#1c1f3d"/>
      <stop offset="0.45" stop-color="#2a2450"/>
      <stop offset="0.6" stop-color="#8a1e3a"/>
      <stop offset="1" stop-color="#1d3c8a"/>
    </linearGradient>
    <linearGradient id="crowd-glow" x1="0" y1="0" x2="0.4" y2="1">
      <stop offset="0" stop-color="#3f9be6"/>
      <stop offset="0.5" stop-color="#2a6fcf"/>
      <stop offset="1" stop-color="#3a3fb8"/>
    </linearGradient>
  </defs>

  <rect class="flyer__frame" width="674" height="871"/>

  <rect x="40" y="40" width="595" height="440" fill="url(#stage-light)"
        role="img" aria-label="Photo of the bass player on stage in a red sleeveless shirt and headband under stage lights"/>

  <polygon points="0,508 411,373 411,361 674,268 674,871 0,871" fill="url(#crowd-glow)"
           role="img" aria-label="Blue-tinted photo of the band performing to a crowd"/>
  <polygon class="panel--light" points="0,508 411,373 411,760 0,840"/>
  <polygon class="panel--strip" points="418,358 674,268 674,700 418,790"/>

  <g class="opening-tagline">
    <text class="headline headline--small" x="624" y="150" text-anchor="end">GRAND OPENING</text>
    <line class="flyer__rule" x1="414" y1="158" x2="624" y2="158"/>
    <text class="headline headline--large" x="624" y="184" text-anchor="end">HOTTEST NEW</text>
    <line class="flyer__rule" x1="414" y1="191" x2="624" y2="191"/>
    <text class="headline headline--large" x="624" y="217" text-anchor="end">BAR IN FRISCO</text>
    <line class="flyer__rule" x1="414" y1="224" x2="624" y2="224"/>
  </g>

  <g class="event-details" transform="translate(31 603) rotate(-22)">
    <text class="venue-name" x="0" y="0" textLength="385" lengthAdjust="spacingAndGlyphs">QUIMBY'S HALL</text>
    <text class="event-line event-line--lead" x="-21" y="40" textLength="381" lengthAdjust="spacingAndGlyphs">PARTY STARTS AT 7:00 PM</text>
    <line class="flyer__rule" x1="-21" y1="48" x2="360" y2="48"/>
    <text class="event-line event-line--detail" x="-30" y="68" textLength="390" lengthAdjust="spacingAndGlyphs">ACOUSTIC SET BY THE VELVET OTTERS</text>
    <text class="event-line event-line--detail" x="-29" y="88" textLength="380" lengthAdjust="spacingAndGlyphs">CORK VALLEY TAKING THE STAGE AT 10:00 PM</text>
    <text class="event-line event-line--promo" x="-16" y="130" textLength="339" lengthAdjust="spacingAndGlyphs">DRINK SPECIALS ALL NIGHT</text>
    <text class="event-line event-line--promo" x="-10" y="153" textLength="330" lengthAdjust="spacingAndGlyphs">WITH THE ZEPHYR PALE GIRLS</text>
    <text class="event-line event-line--promo" x="-4" y="176" textLength="312" lengthAdjust="spacingAndGlyphs">AND GREAT LIVE MUSIC TO</text>
    <text class="event-line event-line--closing" x="4" y="196" textLength="320" lengthAdjust="spacingAndGlyphs">CELEBRATE THIS GRAND OPENING!</text>
  </g>

  <g class="event-date">
    <text class="date date--day" transform="translate(466 453) rotate(-22)" textLength="175" lengthAdjust="spacingAndGlyphs">SAT</text>
    <text class="date date--number" transform="translate(469 583) rotate(-22)" textLength="205" lengthAdjust="spacingAndGlyphs">05</text>
    <text class="date date--month" transform="translate(486 683) rotate(-22)" textLength="168" lengthAdjust="spacingAndGlyphs">APRIL</text>
  </g>

  <text class="band-name" x="572" y="790" text-anchor="middle">CORK VALLEY</text>

  <text class="footer-line" x="337" y="852" text-anchor="middle" textLength="592" lengthAdjust="spacingAndGlyphs">QUIMBY'S HALL. 8241 LARKSPUR AVE. #204, FRISCO, TEXAS. (214) 705-9183 FOR TABLE RESERVATIONS</text>
</svg>
</body>
</html>
```